Business Card for Restaurant Vendal

This project consist of creating 2 design for business card of restaurant named Vendal.

The attached specs below are 'ONLY SUGGESTION' if you have others ideas. You are welcome to post it.

1) Restaurant Card

Adresse:
2784 Côte du Pinard Vert
Montréal (Qc) H4K 3T8

Website:
www.ven-dal.ca

Phone:
438-719-2046

2) Employee Card

Name: Lorna Pik
Title: Owner

Address:
2784 Côte du Pinard Vert
Montréal (Qc) H4K 3T8

Email:lorna@ven-dal.ca
Phone Number:438-719-2046
Cellphone Number:514-830-4162

 The attached specs are 'ONLY SUGGESTION' if you have others ideas.  You are welcome to post it.

Industry/Entity Type

Restaurant

Requirements
Must have
• UV Card Spot

To print Spot UV business cards you would have to submit 2 files for each side. The first file "base" would be your regular design file as it would have been in any other case. The 2nd file "UV mask" is a black/white file. The BLACK color will indicate the areas that will be covered with the UV high gloss finish. To upload the files, please combine front design and front mask file in one P
Nice to have
• 1) The font of the logo should be ink effect
2) black background with wallpaper effect
3) The specs below are 'ONLY SUGGESTION' if you have others ideas. You are welcome to post it.

```html
<!DOCTYPE html>
<html lang="en">
<head>
<meta charset="utf-8">
<title>Restaurant Vendal – Business Cards</title>
<link rel="stylesheet" href="https://fonts.googleapis.com/css2?family=Source+Sans+3:wght@400;600;700;800&display=swap">
<style>
  :root {
    --board-white: #ffffff;
    --band-grey: #333333;
    --card-dark: #1c1c1c;
    --card-dark-2: #262626;
    --card-light: #fbfbfb;
    --ink-black: #111111;
    --lantern-red: #d9211d;
    --text-white: #ffffff;
    --text-dark: #1a1a1a;
  }
  * { margin: 0; padding: 0; box-sizing: border-box; }
  html, body {
    width: 1200px; height: 898px; overflow: hidden;
    background: var(--board-white);
    font-family: "Source Sans 3", "Helvetica Neue", Arial, sans-serif;
  }
  .board { position: relative; width: 1200px; height: 898px; }
  .employee-band {
    position: absolute; left: 0; top: 413px; width: 1200px; height: 420px;
    background: var(--band-grey);
  }
  .card { position: absolute; overflow: hidden; }
  .card--dark {
    background:
      repeating-linear-gradient(90deg, rgba(255,255,255,0.025) 0 1px, transparent 1px 4px),
      linear-gradient(180deg, var(--card-dark-2), var(--card-dark));
  }
  .card--light {
    background:
      repeating-linear-gradient(90deg, rgba(0,0,0,0.018) 0 1px, transparent 1px 5px),
      var(--card-light);
  }
  .restaurant-front { left: 53px; top: 37px; width: 533px; height: 309px; }
  .restaurant-back  { left: 611px; top: 37px; width: 534px; height: 309px; }
  .employee-front   { left: 54px; top: 462px; width: 535px; height: 309px; }
  .employee-back    { left: 615px; top: 462px; width: 536px; height: 309px; }

  .lantern { position: absolute; }
  .restaurant-front .lantern { left: 14px; top: 26px; width: 236px; height: 272px; }
  .restaurant-back .lantern  { left: 250px; top: 8px; width: 265px; height: 295px; }

  .brand { position: absolute; display: flex; align-items: center; gap: 10px; }
  .brand-name { font-weight: 800; letter-spacing: 1px; line-height: 1; }
  .brand-dot { border-radius: 50%; background: var(--lantern-red); flex: none; }
  .tagline { position: absolute; white-space: nowrap; line-height: 1; }

  .restaurant-front .brand { left: 262px; top: 178px; }
  .restaurant-front .brand-name { font-size: 74px; color: var(--text-white); }
  .restaurant-front .brand-dot { width: 16px; height: 16px; }
  .restaurant-front .tagline { left: 281px; top: 270px; font-size: 12.5px; color: var(--text-white); }

  .restaurant-back .contact {
    position: absolute; right: 308px; top: 155px; text-align: right;
    color: var(--text-white); font-size: 16.5px; line-height: 33px;
  }

  .employee-front .brand { left: 112px; top: 92px; }
  .employee-front .brand-name { font-size: 86px; color: var(--ink-black); }
  .employee-front .brand-dot { width: 22px; height: 22px; }
  .employee-front .tagline { left: 133px; top: 198px; font-size: 13px; color: var(--text-dark); }

  .employee-back .brand { left: 34px; top: 112px; }
  .employee-back .brand-name { font-size: 62px; color: var(--ink-black); }
  .employee-back .brand-dot { width: 16px; height: 16px; }
  .employee-back .tagline { left: 50px; top: 189px; font-size: 10.5px; color: var(--text-dark); }

  .dot-rule {
    position: absolute; left: 301px; top: 89px; list-style: none;
  }
  .dot-rule li {
    width: 4px; height: 4px; border-radius: 50%; background: var(--ink-black);
    margin-bottom: 11.2px;
  }
  .person {
    position: absolute; left: 334px; top: 87px;
    font-size: 15px; line-height: 20.2px; color: var(--text-dark);
  }
  .person .person-name { color: var(--lantern-red); font-weight: 600; }
  .person .gap { height: 20px; }

  .card-label { position: absolute; font-size: 22px; line-height: 1; }
  .card-label--restaurant { left: 958px; top: 367px; color: var(--text-dark); }
  .card-label--employee { left: 983px; top: 795px; color: var(--text-white); }
</style>
</head>
<body>
<main class="board">
  <div class="employee-band"></div>

  <section class="card card--dark restaurant-front">
    <svg class="lantern" viewBox="0 0 236 272" role="img" aria-label="Red paper lantern illustration with white hanging loop">
      <ellipse cx="118" cy="160" rx="118" ry="108" fill="var(--lantern-red)"/>
    </svg>
    <div class="brand">
      <span class="brand-name">Vendal</span>
      <span class="brand-dot"></span>
    </div>
    <p class="tagline">Resto-Bar Japonais · Izakaya · 居酒屋</p>
  </section>

  <section class="card card--dark restaurant-back">
    <address class="contact" style="font-style:normal">
      2784 Côte du Pinard Vert<br>
      Montreal (Qc) H4K 3T8<br>
      438-719-2046<br>
      www.ven-dal.ca
    </address>
    <svg class="lantern" viewBox="0 0 265 295" role="img" aria-label="Red paper lantern illustration with white hanging loop and vertical izakaya banner">
      <ellipse cx="132" cy="182" rx="132" ry="112" fill="var(--lantern-red)"/>
    </svg>
  </section>
  <p class="card-label card-label--restaurant">Restaurant Card</p>

  <section class="card card--light employee-front">
    <div class="brand">
      <span class="brand-name">Vendal</span>
      <span class="brand-dot"></span>
    </div>
    <p class="tagline">Resto-Bar Japonais · Izakaya · 居酒屋</p>
  </section>

  <section class="card card--light employee-back">
    <div class="brand">
      <span class="brand-name">Vendal</span>
      <span class="brand-dot"></span>
    </div>
    <p class="tagline">Resto-Bar Japonais · Izakaya · 居酒屋</p>
    <ul class="dot-rule">
      <li></li><li></li><li></li><li></li><li></li><li></li><li></li>
      <li></li><li></li><li></li><li></li><li></li><li></li>
    </ul>
    <div class="person">
      <p class="person-name">Lorna Pik</p>
      <p>Owner</p>
      <div class="gap"></div>
      <p>2784 Côte du Pinard Vert</p>
      <p>Montreal (Qc) H4K 3T8</p>
      <div class="gap"></div>
      <p>lorna@ven-dal.ca</p>
      <p>438-719-2046</p>
      <p>514-830-4162</p>
    </div>
  </section>
  <p class="card-label card-label--employee">Employee Card</p>
</main>
</body>
</html>
```